Ferncrest Dental, LLC business card project

Business card to be designed with current logo.
Dental office- please keep design of card that looks clean and professional.
Please include the following info:
Ferncrest Dental, LLC
Dr. Lorna Pettigrew
2871 Marlowe Street
Bethlehem, PA 18093
610-555-0193
ferncrestdental.office@examplemail.test
Hello everyone-
Reason: Just got back from overseas- will look at all designs and provide feedback. Thank you!
Reason: Polling my friends for the final selection-
thank you to all those that participated- so many talented designers!

```html
<!DOCTYPE html>
<html lang="en">
<head>
<meta charset="utf-8">
<title>Ferncrest Dental, LLC – Business Card</title>
<link rel="stylesheet" href="https://fonts.googleapis.com/css2?family=Questrial&family=Open+Sans:wght@400;800&display=swap">
<style>
  :root {
    --backdrop: #1c1f20;
    --card: #121514;
    --card-edge: #1b1f1e;
    --brand-green: #7cc243;
    --label-green: #8ccf3f;
    --name-grey: #d9dcdc;
    --text-grey: #b4b9b8;
    --art-teal: rgba(60, 170, 170, 0.22);
    --art-green: rgba(130, 195, 60, 0.26);
  }
  * { margin: 0; padding: 0; box-sizing: border-box; }
  html, body { width: 1200px; height: 741px; overflow: hidden; }
  body {
    background: var(--backdrop);
    position: relative;
    font-family: "Open Sans", sans-serif;
  }
  .card {
    position: absolute;
    width: 540px;
    height: 309px;
    background: linear-gradient(160deg, var(--card-edge), var(--card) 60%);
    border-radius: 2px;
    box-shadow: 0 14px 30px rgba(0,0,0,0.55);
    overflow: hidden;
  }
  .card--front { left: 60px; top: 70px; }
  .card--back { left: 600px; top: 362px; }

  .card__art {
    position: absolute;
    top: 0;
    height: 100%;
  }
  .card--front .card__art {
    right: 0;
    width: 140px;
    background: linear-gradient(90deg, transparent, var(--art-teal) 45%, var(--art-green));
  }
  .card--back .card__art {
    left: 0;
    width: 140px;
    background: linear-gradient(270deg, transparent, var(--art-teal) 45%, var(--art-green));
  }

  .brand {
    position: absolute;
    display: flex;
    align-items: center;
    gap: 10px;
  }
  .brand__dot {
    width: 12px; height: 12px;
    border-radius: 50%;
    background: var(--brand-green);
  }
  .brand__name {
    font-family: "Questrial", sans-serif;
    color: var(--brand-green);
    font-size: 32px;
    letter-spacing: -0.5px;
    white-space: nowrap;
  }
  .card--front .brand { left: 34px; top: 160px; }
  .card--back .brand { left: 150px; top: 32px; }
  .card--back .brand__name { font-size: 30px; }

  .person {
    position: absolute;
    left: 172px; top: 94px;
    font-weight: 800;
    font-size: 25px;
    letter-spacing: 1px;
    color: var(--name-grey);
    white-space: nowrap;
  }
  .contact {
    position: absolute;
    left: 172px; top: 148px;
    display: grid;
    grid-template-columns: 58px 12px auto;
    row-gap: 3px;
    font-size: 11.5px;
    line-height: 17px;
    white-space: nowrap;
  }
  .contact__label { color: var(--label-green); }
  .contact__sep { color: var(--text-grey); }
  .contact__value { color: var(--text-grey); letter-spacing: 0.3px; }
</style>
</head>
<body>
  <section class="card card--front">
    <div class="card__art" role="img" aria-label="Decorative artwork area in green and teal tones"></div>
    <div class="brand">
      <span class="brand__dot"></span>
      <span class="brand__name">Ferncrest Dental, LLC</span>
    </div>
  </section>

  <section class="card card--back">
    <div class="card__art" role="img" aria-label="Decorative artwork area in green and teal tones"></div>
    <div class="brand">
      <span class="brand__dot"></span>
      <span class="brand__name">Ferncrest Dental, LLC</span>
    </div>
    <h1 class="person">Dr. Lorna Pettigrew</h1>
    <div class="contact">
      <span class="contact__label">Phone</span><span class="contact__sep">:</span><span class="contact__value">610-555-0193</span>
      <span class="contact__label">Email</span><span class="contact__sep">:</span><span class="contact__value">ferncrestdental.office@examplemail.test</span>
      <span class="contact__label">Address</span><span class="contact__sep">:</span><span class="contact__value">2871 Marlowe Street Bethlehem, PA 18093</span>
    </div>
  </section>
</body>
</html>
```